Business card design needed/logo

Hi I am a cake decorator that makes weddings, birthdays, anniversary cakes, cupcakes etc. I am going to a market next week and need some artwork.

Company Name: BrimBakes

Target Market(s)

im looking for a funky look for my cakes. Something that is simple yet can change colours

Industry/Entity Type

Business

Contact Information for Business Card

cake decorating

Requirements
Nice to have
• I have attached something that I like, the black and floresent lime green is great
Should not have
• I have attached a file of what I like thanks

```html
<!DOCTYPE html>
<html lang="en">
<head>
<meta charset="utf-8">
<title>BrimBakes Business Card</title>
<link rel="stylesheet" href="https://fonts.googleapis.com/css2?family=Arimo:wght@400;700&display=swap">
<style>
  :root {
    --backdrop: #3a3a3a;
    --card: #231f20;
    --lime: #8cc63f;
    --ink-light: #d9d9d9;
    --card-shadow: rgba(0, 0, 0, 0.55);
  }
  * { box-sizing: border-box; margin: 0; padding: 0; }
  html, body {
    width: 1200px;
    height: 900px;
    overflow: hidden;
  }
  body {
    background: var(--backdrop);
    font-family: "Arimo", Arial, sans-serif;
    display: flex;
    flex-direction: column;
    align-items: center;
    justify-content: center;
    gap: 60px;
  }
  .card {
    position: relative;
    width: 560px;
    height: 320px;
    background: var(--card);
    box-shadow: 0 14px 30px var(--card-shadow);
  }

  /* Back of card */
  .card-back .brand {
    position: absolute;
    left: 0;
    right: 0;
    top: 110px;
    display: flex;
    align-items: center;
    justify-content: center;
    gap: 14px;
  }
  .brand-dot {
    width: 22px;
    height: 22px;
    border-radius: 50%;
    background: var(--lime);
  }
  .brand-name {
    color: var(--lime);
    font-weight: 700;
    font-size: 44px;
    letter-spacing: 0.5px;
  }
  .card-back .web-line {
    position: absolute;
    left: 0;
    right: 0;
    bottom: 26px;
    text-align: center;
    color: var(--lime);
    font-size: 13px;
    letter-spacing: 4px;
  }

  /* Front of card */
  .card-front .brand {
    position: absolute;
    left: 34px;
    top: 32px;
    display: flex;
    align-items: center;
    gap: 10px;
  }
  .card-front .brand-dot { width: 16px; height: 16px; }
  .card-front .brand-name { font-size: 34px; }

  .contact-person {
    position: absolute;
    left: 300px;
    top: 170px;
  }
  .person-name {
    color: var(--lime);
    font-size: 19px;
    letter-spacing: 0.5px;
  }
  .person-role {
    color: var(--lime);
    font-size: 10px;
    margin-top: 2px;
    letter-spacing: 0.5px;
  }
  .contact-lines {
    position: absolute;
    left: 300px;
    top: 228px;
    list-style: none;
    font-size: 11.5px;
    line-height: 19px;
    letter-spacing: 1.2px;
  }
  .contact-label { color: var(--lime); }
  .contact-value { color: var(--ink-light); }

  .address {
    position: absolute;
    left: 34px;
    top: 210px;
    font-size: 11px;
    line-height: 16px;
    letter-spacing: 1.2px;
    font-style: normal;
  }
  .address .contact-label { display: block; margin-bottom: 2px; }
</style>
</head>
<body>

  <section class="card card-back" aria-label="Business card back">
    <div class="brand">
      <span class="brand-dot"></span>
      <span class="brand-name">BrimBakes</span>
    </div>
    <p class="web-line">www.brimbakes.com</p>
  </section>

  <section class="card card-front" aria-label="Business card front">
    <div class="brand">
      <span class="brand-dot"></span>
      <span class="brand-name">BrimBakes</span>
    </div>

    <address class="address">
      <span class="contact-label">Address:</span>
      <span class="contact-value">48 Baker Lane, Millbrook,<br>Eastvale District, E4V2BK</span>
    </address>

    <div class="contact-person">
      <p class="person-name">Mara Tolley</p>
      <p class="person-role">Designer</p>
    </div>

    <ul class="contact-lines">
      <li><span class="contact-label">Phone:</span> <span class="contact-value">01 5550 2417</span></li>
      <li><span class="contact-label">Email:</span> <span class="contact-value">hello@brimbakes.com</span></li>
      <li><span class="contact-label">Web:</span> <span class="contact-value">www.brimbakes.com</span></li>
    </ul>
  </section>

</body>
</html>
```